Newspaper Ad for Front page strip

Corvel Quick Lending is a micro lender operating in the Caribbean. This ad is for our Trinidad and Tobago location.
Would like to design a catchy banner ad for the front page of a daily newspaper. The ad should capture 1) that we offer unsecured loans up to $40,000. 2) customer can apply online or over the phone 3) that the process is quick.
We have included the a snapshot of our Instagram posts as well as the newspaper location and size of the ad.
We have booked this ad spot for the year so the more engaging we can make it the better. Maybe we can do a series of ads or weekly storyline . Let’s be creative.
https://www.instagram.com/corvelquicklending/
www.corvelquick lending.example
Target Market(s)
Mass population.
Industry/Entity Type
Banking
Look and feel

```html
<!DOCTYPE html>
<html lang="en">
<head>
<meta charset="utf-8">
<title>Corvel Quick Lending – Front Page Strip Series</title>
<link rel="stylesheet" href="https://fonts.googleapis.com/css2?family=Montserrat:wght@800&family=Mulish:wght@600;700&family=Oswald:wght@300;400;500&family=Questrial&display=swap">
<style>
  :root {
    --canvas: #e5e6e8;
    --green: #3d8f4a;
    --green-dark: #2f7a3c;
    --red: #e3312b;
    --ink: #222;
    --grey: #444;
    --wash-top: #ffffff;
    --wash-mid: #eef6dd;
    --wash-low: #c6e29a;
  }
  * { box-sizing: border-box; margin: 0; padding: 0; }
  html, body { width: 1200px; height: 1200px; overflow: hidden; background: var(--canvas); }
  .stage { position: relative; width: 1200px; height: 1200px; }

  .strip {
    position: absolute;
    width: 296px; height: 1300px;
    transform: scale(0.8); transform-origin: 0 0;
    border: 2px solid var(--green);
    background:
      radial-gradient(ellipse 120% 40% at 0% 75%, rgba(160,210,100,.45), transparent 70%),
      radial-gradient(ellipse 90% 30% at 100% 95%, rgba(190,220,110,.5), transparent 70%),
      linear-gradient(180deg, var(--wash-top) 0%, var(--wash-top) 35%, var(--wash-mid) 55%, var(--wash-low) 100%);
    overflow: hidden;
    text-align: center;
    color: var(--ink);
  }
  .strip--money-tree { left: 110px; top: 80px; }
  .strip--rain { left: 477px; top: 87px; box-shadow: 4px 4px 6px rgba(0,0,0,.18); }
  .strip--smile { left: 840px; top: 88px; box-shadow: 4px 4px 6px rgba(0,0,0,.18); }

  .brand {
    position: absolute; left: 0; right: 0; top: 26px;
    display: flex; flex-direction: column; align-items: center;
  }
  .brand__name {
    font-family: "Mulish", sans-serif; font-weight: 700;
    font-size: 25px; line-height: 28px; color: var(--green);
  }

  .visual { position: absolute; }
  .visual--money-tree { left: 60px; top: 130px; width: 176px; height: 265px; border-radius: 6px;
    background: radial-gradient(ellipse at 50% 70%, #a88a62 0%, #c9b28c 35%, #dfeed0 70%, #ffffff 100%); }
  .visual--rain { left: 0; top: 228px; width: 292px; height: 308px;
    background: radial-gradient(ellipse at 50% 45%, #6a4a33 0%, #3fae88 38%, #d9efe0 72%, #ffffff 100%); }
  .visual--smile { left: 0; top: 208px; width: 292px; height: 297px;
    background: linear-gradient(135deg, #2a1a12 0%, #7a5138 45%, #c9c4a8 70%, #e8e6dc 100%); }

  .headline {
    position: absolute; left: 8px; right: 8px;
    font-family: "Mulish", sans-serif; font-weight: 600;
    font-size: 24px; line-height: 30px; color: var(--red);
  }
  .headline .g { color: var(--green); }
  .strip--money-tree .headline { top: 410px; }
  .strip--rain .headline { top: 128px; }
  .strip--smile .headline { top: 128px; }

  .lede {
    position: absolute; left: 10px; right: 10px;
    font-family: "Questrial", sans-serif; font-size: 21px; line-height: 28px; color: var(--ink);
  }
  .lede b { font-family: "Mulish", sans-serif; font-weight: 700; font-size: 20px; }
  .strip--money-tree .lede { top: 522px; }
  .strip--rain .lede { top: 552px; }
  .strip--smile .lede { top: 552px; }

  .offer { position: absolute; left: 0; right: 0; }
  .strip--money-tree .offer { top: 660px; }
  .strip--rain .offer, .strip--smile .offer { top: 677px; }

  .offer__loans { font-family: "Montserrat", sans-serif; font-weight: 800; font-size: 23px; line-height: 31px; color: var(--red); }
  .offer__loans span { color: var(--green); display: block; }

  .offer__steps { margin-top: 20px; font-family: "Questrial", sans-serif; font-size: 23px; line-height: 30px; letter-spacing: .6px; }
  .offer__steps .r { color: var(--red); }
  .offer__steps .g { color: var(--green); display: block; }

  .apply {
    display: inline-block; margin-top: 34px;
    font-family: "Oswald", sans-serif; font-weight: 400; font-size: 18px; line-height: 26px;
    color: #fff; background: var(--red); border: 2px solid #fff; border-radius: 14px;
    padding: 0 14px; box-shadow: 0 0 0 1px var(--red);
  }
  .call { margin-top: 22px; font-family: "Oswald", sans-serif; font-weight: 400; font-size: 23px; color: var(--green-dark); }
  .call span { color: var(--red); }
  .visit { margin-top: 16px; font-family: "Oswald", sans-serif; font-weight: 300; font-size: 17px; color: var(--grey); }

  .locations { list-style: none; margin-top: 12px; font-family: "Oswald", sans-serif; font-weight: 300; font-size: 18px; line-height: 31px; color: var(--grey); }
  .locations li::before { content: "•"; color: var(--red); margin-right: 5px; }

  .contact { margin-top: 16px; font-family: "Oswald", sans-serif; font-weight: 500; font-size: 18px; line-height: 20px; color: var(--red); }
  .contact svg { display: block; margin: 0 auto; }
  .contact p { margin-bottom: 2px; }
</style>
</head>
<body>
<main class="stage">

  <section class="strip strip--money-tree">
    <div class="brand"><div class="brand__name">Corvel<br>Quick Lending</div></div>
    <div class="visual visual--money-tree" role="img" aria-label="Young money tree growing from a burlap sack marked with a dollar sign"></div>
    <h2 class="headline">Have you ever wished for a <span class="g">Money Tree</span> in your backyard?</h2>
    <p class="lede">Well, we haven’t got those as yet but we can provide you with <b>financial solutions:</b></p>
    <div class="offer">
      <p class="offer__loans">UNSECURED LOANS<span>up to $40,000.!</span></p>
      <p class="offer__steps"><span class="r">Quick</span> and <span class="r">Easy</span><br>application online<br>or via telephone.<span class="g">No Hassle. No Sweat.</span></p>
      <span class="apply">Apply Now</span>
      <p class="call">Call us at <span>224-4CQL (4275)</span></p>
      <p class="visit">or Visit any of our five locations:</p>
      <ul class="locations">
        <li>18 Mango Lane, Chaguanas</li>
        <li>9 Orchid Street, Arima</li>
        <li>3 Bay Court, Scarborough, Tobago</li>
        <li>52 Harbour Road, San Fernando</li>
        <li>120 Lantern Street, Port of Spain</li>
      </ul>
      <div class="contact">
        <svg width="16" height="16" viewBox="0 0 16 16"><g fill="none" stroke="#e3312b" stroke-width="1.3"><circle cx="8" cy="8" r="6.5"/><ellipse cx="8" cy="8" rx="3" ry="6.5"/><path d="M1.5 8h13M2.5 4.5h11M2.5 11.5h11"/></g></svg>
        <p>www.corvelquick lending.example</p>
        <svg width="12" height="12" viewBox="0 0 12 12"><circle cx="6" cy="6" r="5" fill="#e3312b"/></svg>
        <p>corvelquicklending/</p>
      </div>
    </div>
  </section>

  <section class="strip strip--rain">
    <div class="brand"><div class="brand__name">Corvel<br>Quick Lending</div></div>
    <h2 class="headline"><span class="g">Today’s Weather Forecast: It’s going to</span> rain money!</h2>
    <div class="visual visual--rain" role="img" aria-label="Joyful woman in a green top with banknotes falling around her"></div>
    <p class="lede">Well, not exactly, but we can provide you with <b>financial solutions:</b></p>
    <div class="offer">
      <p class="offer__loans">UNSECURED LOANS<span>up to $40,000.!</span></p>
      <p class="offer__steps"><span class="r">Quick</span> and <span class="r">Easy</span><br>application online<br>or via telephone.<span class="g">No Hassle. No Sweat.</span></p>
      <span class="apply">Apply Now</span>
      <p class="call">Call us at <span>224-4CQL (4275)</span></p>
      <p class="visit">or Visit any of our five locations:</p>
      <ul class="locations">
        <li>18 Mango Lane, Chaguanas</li>
        <li>9 Orchid Street, Arima</li>
        <li>3 Bay Court, Scarborough, Tobago</li>
        <li>52 Harbour Road, San Fernando</li>
        <li>120 Lantern Street, Port of Spain</li>
      </ul>
      <div class="contact">
        <svg width="16" height="16" viewBox="0 0 16 16"><g fill="none" stroke="#e3312b" stroke-width="1.3"><circle cx="8" cy="8" r="6.5"/><ellipse cx="8" cy="8" rx="3" ry="6.5"/><path d="M1.5 8h13M2.5 4.5h11M2.5 11.5h11"/></g></svg>
        <p>www.corvelquick lending.example</p>
        <svg width="12" height="12" viewBox="0 0 12 12"><circle cx="6" cy="6" r="5" fill="#e3312b"/></svg>
        <p>corvelquicklending/</p>
      </div>
    </div>
  </section>

  <section class="strip strip--smile">
    <div class="brand"><div class="brand__name">Corvel<br>Quick Lending</div></div>
    <h2 class="headline"><span class="g">Need something to</span><br>smile about?</h2>
    <div class="visual visual--smile" role="img" aria-label="Woman holding a fan of banknotes up to her face"></div>
    <p class="lede">Take advantage of our <b>financial solutions offer</b> and step on up.</p>
    <div class="offer">
      <p class="offer__loans">UNSECURED LOANS<span>up to $40,000.!</span></p>
      <p class="offer__steps"><span class="r">Quick</span> and <span class="r">Easy</span><br>application online<br>or via telephone.<span class="g">No Hassle. No Sweat.</span></p>
      <span class="apply">Apply Now</span>
      <p class="call">Call us at <span>224-4CQL (4275)</span></p>
      <p class="visit">or Visit any of our five locations:</p>
      <ul class="locations">
        <li>18 Mango Lane, Chaguanas</li>
        <li>9 Orchid Street, Arima</li>
        <li>3 Bay Court, Scarborough, Tobago</li>
        <li>52 Harbour Road, San Fernando</li>
        <li>120 Lantern Street, Port of Spain</li>
      </ul>
      <div class="contact">
        <svg width="16" height="16" viewBox="0 0 16 16"><g fill="none" stroke="#e3312b" stroke-width="1.3"><circle cx="8" cy="8" r="6.5"/><ellipse cx="8" cy="8" rx="3" ry="6.5"/><path d="M1.5 8h13M2.5 4.5h11M2.5 11.5h11"/></g></svg>
        <p>www.corvelquick lending.example</p>
        <svg width="12" height="12" viewBox="0 0 12 12"><circle cx="6" cy="6" r="5" fill="#e3312b"/></svg>
        <p>corvelquicklending/</p>
      </div>
    </div>
  </section>

</main>
</body>
</html>
```